Checkout sign

Wall sign for clinic checkout.
“The Good Lord does ALL the healing..
But we DO collect the co-pay”

Add Celtic cross at top and our logo on bottom

```html
<!DOCTYPE html>
<html lang="en">
<head>
<meta charset="utf-8">
<title>Checkout Sign – Hallowell Orthopedic Clinic</title>
<link href="https://fonts.googleapis.com/css2?family=Caladea:wght@400;700&display=swap" rel="stylesheet">
<style>
  :root {
    --page-bg: #e6e6e8;
    --ink: #37278a;
    --sky-white: #ffffff;
    --sky-grey: #cdd5e2;
    --sky-blue: #a9d9ee;
    --cross-light: #5a45b0;
    --cross-dark: #33227f;
  }
  * { margin: 0; padding: 0; box-sizing: border-box; }
  html, body {
    width: 1200px;
    height: 2288px;
    overflow: hidden;
    background: var(--page-bg);
  }
  .sign {
    position: absolute;
    left: 50px;
    top: 366px;
    width: 1100px;
    height: 1556px;
    overflow: hidden;
    background:
      radial-gradient(ellipse 60% 38% at 50% 22%, var(--sky-white) 0%, rgba(255,255,255,0.85) 45%, rgba(255,255,255,0) 100%),
      radial-gradient(ellipse 70% 35% at 12% 62%, rgba(169,217,238,0.9) 0%, rgba(169,217,238,0) 100%),
      radial-gradient(ellipse 60% 30% at 92% 60%, rgba(150,210,236,0.9) 0%, rgba(150,210,236,0) 100%),
      radial-gradient(ellipse 80% 30% at 50% 82%, rgba(190,228,243,0.8) 0%, rgba(190,228,243,0) 100%),
      linear-gradient(180deg, var(--sky-grey) 0%, #eef2f7 28%, #e4f3fa 55%, #d7eef8 75%, #f4fafd 100%);
  }
  .sign__cross {
    position: absolute;
    left: 389px;
    top: 75px;
    width: 322px;
    height: 504px;
    background: linear-gradient(180deg, var(--cross-light), var(--cross-dark));
    border-radius: 6px;
    opacity: 0.9;
  }
  .sign__message {
    position: absolute;
    left: 0;
    top: 668px;
    width: 100%;
    text-align: center;
    font-family: "Caladea", "Cambria", serif;
    font-weight: 700;
    font-size: 82px;
    line-height: 103px;
    color: var(--ink);
  }
  .sign__brand {
    position: absolute;
    left: 0;
    top: 1215px;
    width: 100%;
    text-align: center;
    color: var(--ink);
    font-family: "Caladea", "Cambria", serif;
    font-weight: 400;
  }
  .sign__brand-mark {
    display: block;
    margin: 0 auto 22px;
    width: 172px;
    height: 172px;
  }
  .sign__brand-name {
    font-size: 52px;
    line-height: 52px;
    letter-spacing: 1px;
  }
  .sign__brand-tagline {
    font-size: 23px;
    line-height: 30px;
    letter-spacing: 2px;
  }
</style>
</head>
<body>
  <main class="sign">
    <div class="sign__cross" role="img" aria-label="Celtic cross with knotwork, set against a burst of light"></div>

    <p class="sign__message">
      The Good Lord<br>
      does ALL the healing..<br>
      But we DO collect<br>
      the co-pay
    </p>

    <div class="sign__brand">
      <svg class="sign__brand-mark" viewBox="0 0 172 172" aria-hidden="true">
        <circle cx="86" cy="86" r="80" fill="none" stroke="var(--ink)" stroke-width="8"/>
      </svg>
      <div class="sign__brand-name">HALLOWELL</div>
      <div class="sign__brand-tagline">ORTHOPEDIC CLINIC</div>
    </div>
  </main>
</body>
</html>
```